Business Card Design

We are a motorcycle parts, spares, accessories and workshop as well as a vq dealership. We mostly specialize in dirt bikes. I have uploaded a pic of bikes lined up at the starting gate. I envisage having the picture as a backboard maybe out of focus with the logo at the top of the card and the details off to the right side.

Target Market(s)

Male Motorcycle enthusiast aged 18-35

Industry/Entity Type

Business

Contact Information for Business Card

8/314 Pelican Ridge Rd
Harlow Creek QLD 4119
Ph: (07) 3902 4157
Email: lorna@kerbstonegear.com.au
www.kerbstonegear.com.au

Requirements
Must have
• on the rear side of the card lines for writing

```html
<!DOCTYPE html>
<html lang="en">
<head>
<meta charset="utf-8">
<title>Kerbstone Gear – Business Card</title>
<link href="https://fonts.googleapis.com/css2?family=Open+Sans:wght@400;600;800&display=swap" rel="stylesheet">
<style>
  :root {
    --stage: #111719;
    --card: #ffffff;
    --ink: #111111;
    --rule: #8a8a8a;
    --photo-red: #c9566a;
    --photo-pink: #e7a3b0;
    --photo-grey: #b9b6bd;
    --photo-lilac: #a9a6d8;
    --band: rgba(255, 255, 255, 0.55);
  }
  html, body {
    margin: 0;
    width: 1200px;
    height: 800px;
    overflow: hidden;
    background: var(--stage);
    font-family: "Open Sans", Arial, sans-serif;
  }
  .sheet {
    position: relative;
    width: 1200px;
    height: 800px;
  }
  .card {
    position: absolute;
    background: var(--card);
    overflow: hidden;
  }
  .card--front {
    left: 105px;
    top: 244px;
    width: 477px;
    height: 309px;
  }
  .card--back {
    left: 616px;
    top: 245px;
    width: 480px;
    height: 312px;
  }
  .backdrop-photo {
    position: absolute;
    inset: 0;
    background:
      linear-gradient(90deg, rgba(255,255,255,0) 0%, rgba(255,255,255,0) 45%, rgba(255,255,255,0.85) 80%, #fff 100%),
      linear-gradient(180deg, var(--photo-lilac) 0%, rgba(169,166,216,0) 30%),
      linear-gradient(135deg, var(--photo-red) 0%, var(--photo-grey) 35%, var(--photo-pink) 60%, var(--photo-red) 85%);
  }
  .brand-band {
    position: absolute;
    left: 0;
    top: 117px;
    width: 440px;
    height: 45px;
    background: var(--band);
  }
  .brand {
    position: absolute;
    right: 34px;
    top: 118px;
    display: flex;
    align-items: center;
    gap: 8px;
  }
  .brand__name {
    font-weight: 800;
    font-size: 30px;
    letter-spacing: 0.5px;
    text-transform: uppercase;
    color: var(--ink);
    line-height: 1;
  }
  .brand__mark {
    width: 22px;
    height: 22px;
    background: var(--ink);
  }
  .tagline {
    position: absolute;
    right: 42px;
    top: 160px;
    font-weight: 800;
    font-size: 10px;
    letter-spacing: 0.6px;
    text-transform: uppercase;
    color: var(--ink);
  }
  .contact {
    position: absolute;
    right: 36px;
    top: 196px;
    text-align: right;
    font-style: normal;
    font-size: 14.5px;
    line-height: 14.5px;
    letter-spacing: -0.6px;
    color: var(--ink);
  }
  .contact p { margin: 0; }
  .contact .gap { margin-top: 12px; }
  .write-lines {
    position: absolute;
    left: 30px;
    top: 65px;
    width: 417px;
  }
  .write-lines span {
    display: block;
    height: 33.6px;
    border-bottom: 1px dotted var(--rule);
  }
  .write-lines span:first-child { height: 0; }
</style>
</head>
<body>
  <main class="sheet">
    <section class="card card--front">
      <div class="backdrop-photo" role="img" aria-label="Blurred photo of dirt bikes lined up at the starting gate"></div>
      <div class="brand-band"></div>
      <div class="brand">
        <span class="brand__name">Kerbstone Gear</span>
        <span class="brand__mark"></span>
      </div>
      <div class="tagline">Repairs - Sales - Service</div>
      <address class="contact">
        <p>8/314 Pelican Ridge Rd</p>
        <p>Harlow Creek QLD 4119</p>
        <p class="gap">Ph: (07) 3902 4157</p>
        <p>Email: lorna@kerbstonegear.com.au</p>
        <p>www.kerbstonegear.com.au</p>
      </address>
    </section>
    <section class="card card--back">
      <div class="write-lines">
        <span></span><span></span><span></span><span></span><span></span><span></span><span></span><span></span>
      </div>
    </section>
  </main>
</body>
</html>
```